Halvern Crest Training PowerPoint Template

I want to PowerPoint template theme using my attached logo. My colors are black and orange. My website is HalvernCrest.com. I am a handgun training company.

Font:

- Serpentine-Bold-Bold for "DORN VALE"

- BrowalliaUPC for "SHOOTING SPORTS"

Colors (CMYK code):

- BLACK ....... 0; 0; 0; 100;
- ORANGE ... gradient from 0; 65; 97.5; 0 to 0; 39; 97.5; 0

```html
<!DOCTYPE html>
<html lang="en">
<head>
<meta charset="utf-8">
<title>Halvern Crest Training – Presentation Templates</title>
<link rel="stylesheet" href="https://fonts.googleapis.com/css2?family=Archivo+Black&family=Arimo:ital,wght@0,400;0,700;1,700&family=Russo+One&display=swap">
<style>
  :root {
    --black: #000000;
    --panel: #111111;
    --orange-deep: #e5801c;
    --orange-light: #f2b705;
    --gold-text: #ecb30f;
    --white: #ffffff;
    --ink: #1a1a1a;
    --cream: #fde7a8;
    --stone-a: #b3bba4;
    --stone-b: #8f9b82;
  }
  * { margin: 0; padding: 0; box-sizing: border-box; }
  html, body { width: 810px; height: 1200px; overflow: hidden; }
  body { position: relative; font-family: "Arimo", Arial, sans-serif; }

  .backdrop {
    position: absolute; inset: 0;
    background: radial-gradient(ellipse at 40% 40%, var(--stone-a), var(--stone-b));
  }
  .section-label {
    position: absolute; left: 0; width: 810px; text-align: center;
    color: var(--white); font-size: 25px;
    text-shadow: 0 1px 3px rgba(0,0,0,.55);
  }
  .section-label.main { top: 16px; }
  .section-label.secondary { top: 586px; }

  .brand-mark {
    position: absolute; display: flex; flex-direction: column; align-items: center; justify-content: center;
    gap: 4px; text-align: center;
    font-family: "Arimo", Arial, sans-serif; font-weight: 700; color: var(--black); line-height: 1.1;
  }
  .brand-mark .dot { width: 18px; height: 18px; border-radius: 50%; background: var(--black); }

  /* Main slide */
  .title-slide { position: absolute; left: 60px; top: 58px; width: 690px; height: 517px; background: var(--panel); }
  .title-slide .header {
    position: absolute; left: 0; top: 0; width: 690px; height: 104px;
    background: linear-gradient(90deg, var(--orange-deep), var(--orange-light) 50%, var(--orange-deep));
    border-bottom: 4px solid #b48a3a;
  }
  .title-slide .brand-mark { left: 12px; top: 10px; width: 96px; height: 84px; font-size: 11px; }
  .company-name { position: absolute; left: 140px; width: 510px; text-align: center; color: var(--ink); font-size: 29px; letter-spacing: .5px; }
  .company-name b { font-family: "Archivo Black", sans-serif; font-weight: 400; }
  .title-slide .company-name { top: 22px; }
  .company-url { position: absolute; left: 140px; top: 62px; width: 510px; text-align: center; color: var(--ink); font-size: 16px; }
  .title-slide .body {
    position: absolute; left: 0; top: 108px; width: 690px; height: 371px;
    background: radial-gradient(ellipse at 50% 40%, #1c1c1c, #060606);
  }
  .presentation-title {
    position: absolute; left: 0; top: 230px; width: 690px; text-align: center;
    font-family: "Russo One", sans-serif; font-size: 40px; color: var(--gold-text); letter-spacing: 1px;
  }
  .presentation-subtitle { position: absolute; left: 0; top: 312px; width: 690px; text-align: center; color: var(--white); font-size: 24px; }
  .title-slide .footer {
    position: absolute; left: 0; top: 479px; width: 690px; height: 38px;
    background: var(--black); border-top: 3px solid var(--orange-deep);
    color: var(--white); font-size: 15px;
  }
  .footer .date { position: absolute; left: 13px; top: 9px; }
  .footer .presenter { position: absolute; left: 0; width: 690px; top: 9px; text-align: center; font-weight: 700; }
  .footer .job { position: absolute; right: 12px; top: 9px; }

  /* Content slide */
  .content-slide {
    position: absolute; left: 60px; top: 628px; width: 690px; height: 519px;
    background: linear-gradient(180deg, var(--white) 55%, var(--cream));
    overflow: hidden;
  }
  .content-slide .topbar { position: absolute; left: 0; top: 0; width: 690px; height: 65px; background: var(--black); }
  .slide-heading { position: absolute; left: 12px; top: 14px; }
  .slide-heading span {
    position: absolute; left: 12px; top: 7px; white-space: nowrap;
    font-family: "Russo One", sans-serif; font-size: 20px; color: var(--white); letter-spacing: .5px;
  }
  .faint-brand {
    position: absolute; left: 470px; top: 200px; width: 240px; text-align: center;
    font-family: "Arimo", Arial, sans-serif; font-weight: 700; font-size: 36px; line-height: 1.1; color: rgba(0,0,0,.05);
  }
  .rules { position: absolute; left: 48px; top: 150px; list-style: none; }
  .rules li {
    position: relative; padding-left: 43px; margin-bottom: 18px; width: 470px;
    font-weight: 700; font-style: italic; font-size: 17px; line-height: 28px; color: var(--ink);
  }
  .rules svg { position: absolute; left: 0; top: 3px; }
  .content-slide .brand-mark { left: 12px; top: 440px; width: 68px; height: 64px; font-size: 9px; z-index: 2; }
  .content-slide .footbar { position: absolute; left: 0; top: 477px; }
  .content-slide .company-name { left: 100px; top: 485px; width: auto; color: var(--white); font-size: 21px; }
  .page-number { position: absolute; right: 22px; top: 479px; color: var(--white); font-family: "Arimo", sans-serif; font-weight: 700; font-size: 30px; }
</style>
</head>
<body>
  <div class="backdrop" role="img" aria-label="Weathered green-grey stone texture background"></div>

  <div class="section-label main">Main Template</div>

  <section class="title-slide">
    <div class="header">
      <div class="brand-mark"><span class="dot"></span>HALVERN CREST TRAINING</div>
      <div class="company-name"><b>HALVERN CREST</b> TRAINING</div>
      <div class="company-url">www.halverncrest.com</div>
    </div>
    <div class="body">
      <div class="presentation-title" style="top:122px">PRESENTATION TITLE</div>
      <div class="presentation-subtitle" style="top:204px">Presentation Subtitle</div>
    </div>
    <div class="footer">
      <span class="date">16 February 2014</span>
      <span class="presenter">PRESENTOR’S NAME</span>
      <span class="job">Job Title</span>
    </div>
  </section>

  <div class="section-label secondary">Secondary Template</div>

  <section class="content-slide">
    <div class="topbar"></div>
    <div class="slide-heading">
      <svg width="552" height="40" viewBox="0 0 552 40">
        <defs>
          <linearGradient id="tabFill" x1="0" x2="1">
            <stop offset="0" stop-color="#e5801c"/><stop offset="1" stop-color="#f2b705"/>
          </linearGradient>
        </defs>
        <polygon points="0,0 525,0 552,40 0,40" fill="url(#tabFill)"/>
      </svg>
      <span>THE 4 GUN SAFETY RULES</span>
    </div>

    <div class="faint-brand">HALVERN CREST TRAINING</div>

    <ul class="rules">
      <li><svg width="24" height="24" viewBox="0 0 24 24"><circle cx="12" cy="12" r="10" fill="#bbb"/><circle cx="12" cy="12" r="6" fill="#666"/><circle cx="12" cy="12" r="3.5" fill="#111"/></svg>All guns are ALWAYS loaded</li>
      <li><svg width="24" height="24" viewBox="0 0 24 24"><circle cx="12" cy="12" r="10" fill="#bbb"/><circle cx="12" cy="12" r="6" fill="#666"/><circle cx="12" cy="12" r="3.5" fill="#111"/></svg>ALWAYS keep your finger off the trigger until ready to shoot.</li>
      <li><svg width="24" height="24" viewBox="0 0 24 24"><circle cx="12" cy="12" r="10" fill="#bbb"/><circle cx="12" cy="12" r="6" fill="#666"/><circle cx="12" cy="12" r="3.5" fill="#111"/></svg>NEVER point the gun at anything you are not willing to destroy.</li>
      <li><svg width="24" height="24" viewBox="0 0 24 24"><circle cx="12" cy="12" r="10" fill="#bbb"/><circle cx="12" cy="12" r="6" fill="#666"/><circle cx="12" cy="12" r="3.5" fill="#111"/></svg>ALWAYS know your target and what is beyond.</li>
    </ul>

    <svg class="footbar" width="690" height="42" viewBox="0 0 690 42">
      <defs>
        <linearGradient id="pageFill" x1="0" x2="1">
          <stop offset="0" stop-color="#e5801c"/><stop offset="1" stop-color="#f2a40c"/>
        </linearGradient>
      </defs>
      <rect x="0" y="0" width="690" height="42" fill="url(#pageFill)"/>
      <polygon points="0,0 590,0 630,42 0,42" fill="#000"/>
    </svg>
    <div class="brand-mark"><span class="dot"></span>HALVERN CREST TRAINING</div>
    <div class="company-name"><b>HALVERN CREST</b> TRAINING</div>
    <div class="page-number">01</div>
  </section>
</body>
</html>
```